Wine label for South African wine

modern, creative wine label name: Vaalbrook The Marivel-Trade GmbH - Sundry Vintners one of the leading independent providers of inexpensive wines from around the world. The company focuses entirely on this dynamic, constantly evolving wine market, and our customers can therefore take full advantage of a complete supply chain management for themselves, including: * http://www.marivelhandel.de/img/blatt.jpg procuring wines from the major producing regions around the globe * logistics and processing * wage filling and packaging * dealcoholization of wines for gastronomic purposes * design of exclusive client and proprietary brands, the target market / target group: the International market design Features; Modern, simple, meaningful, unique; Colors: gold, black, red;

Target Market(s)

Off Trade

Industry/Entity Type

Union

Font styles to use
Serif
Script

Requirements
Must have
• Modern, simple, meaningful, unique colors: gold, black, red varieties: Cab Sauv, Chard, Chenin, Merlot, Merlot Rose, Pinotage, Pinotage Rose, Shiraz, Red, Rose, White Non transparent max. Size: 12 x 9 cm data on VE: name brand, variety, country; WITHOUT Year

```html
<!DOCTYPE html>
<html lang="en">
<head>
<meta charset="utf-8">
<title>Vaalbrook Pinotage – Label Range</title>
<link href="https://fonts.googleapis.com/css2?family=Bodoni+Moda:wght@400;500&family=Pinyon+Script&display=swap" rel="stylesheet">
<style>
  :root {
    --stage: #cfcfcf;
    --stage-light: #e2e2e2;
    --paper-cream: #ede5c9;
    --paper-black: #1d1c1b;
    --gold: #a8875c;
    --gold-bright: #c9a977;
    --gold-deep: #6f5433;
    --wine-red: #b3123b;
    --ink: #161514;
    --rule-light: #bdbab3;
  }
  * { box-sizing: border-box; margin: 0; padding: 0; }
  html, body {
    width: 1200px;
    height: 800px;
    overflow: hidden;
  }
  body {
    background: radial-gradient(ellipse at 50% 40%, var(--stage-light), var(--stage));
    display: flex;
    align-items: center;
    justify-content: space-evenly;
    font-family: "Bodoni Moda", "Didot", serif;
  }
  .label {
    width: 330px;
    height: 400px;
    display: flex;
    flex-direction: column;
    align-items: center;
    padding-top: 44px;
    box-shadow: 0 6px 18px rgba(0,0,0,0.18);
  }
  .label--cream {
    background:
      repeating-linear-gradient(0deg, rgba(120,100,60,0.05) 0 1px, transparent 1px 3px),
      var(--paper-cream);
  }
  .label--black {
    background:
      repeating-linear-gradient(0deg, rgba(255,255,255,0.025) 0 1px, transparent 1px 3px),
      var(--paper-black);
  }
  .brand {
    font-size: 31px;
    font-weight: 400;
    letter-spacing: 0.06em;
    text-transform: uppercase;
    color: var(--gold);
  }
  .label--black .brand { color: var(--gold-bright); }
  .emblem {
    margin-top: 22px;
    width: 118px;
    height: 134px;
    border-radius: 46% 46% 40% 40%;
    background: radial-gradient(ellipse at 45% 40%, var(--gold-bright), var(--gold) 55%, var(--gold-deep));
    opacity: 0.75;
  }
  .label--black .emblem { opacity: 0.95; }
  .variety {
    margin-top: 26px;
    font-size: 33px;
    font-weight: 500;
    letter-spacing: 0.03em;
    color: var(--wine-red);
  }
  .rule {
    width: 196px;
    height: 1.5px;
    margin-top: 6px;
    background: var(--ink);
  }
  .label--black .rule { background: var(--rule-light); }
  .origin {
    margin-top: 12px;
    font-size: 19px;
    color: var(--ink);
  }
  .origin--script {
    font-family: "Pinyon Script", cursive;
    font-size: 30px;
    margin-top: 4px;
  }
  .label--black .origin { color: var(--rule-light); }
</style>
</head>
<body>
  <section class="label label--cream">
    <h1 class="brand">Vaalbrook</h1>
    <div class="emblem" role="img" aria-label="Embossed gold illustration of a lion-head door knocker"></div>
    <p class="variety">PINOTAGE</p>
    <div class="rule"></div>
    <p class="origin">South Africa</p>
  </section>

  <section class="label label--black">
    <h1 class="brand">Vaalbrook</h1>
    <div class="emblem" role="img" aria-label="Gold foil illustration of a lion-head door knocker"></div>
    <p class="variety">PINOTAGE</p>
    <div class="rule"></div>
    <p class="origin origin--script">South Africa</p>
  </section>

  <section class="label label--cream">
    <h1 class="brand">Vaalbrook</h1>
    <div class="emblem" role="img" aria-label="Embossed gold illustration of a lion-head door knocker"></div>
    <p class="variety">PINOTAGE</p>
    <div class="rule"></div>
    <p class="origin origin--script">South Africa</p>
  </section>
</body>
</html>
```